Design bcard for Lumerant Advising and Coaching LLC

I need a logo inspired by the term Lumerant. I'd like to have type of work I do on the back side, i.e. provide C and T on DEIJ, SDOH,...... Front of card--business name, contact information, and possibly a tag line.

Target Market(s)

NGOs, human service agencies, education, healthcare, public health.

Contact Information for Business Card

Name of business, email address, phone number, logo--on front. Services on the back

Font styles to use
Sans Serif

Requirements
Must have
• Contact information, creative logo, services

```html
<!DOCTYPE html>
<html lang="en">
<head>
<meta charset="utf-8">
<title>Lumerant Advising and Coaching LLC — Business Card</title>
<link href="https://fonts.googleapis.com/css2?family=Josefin+Sans:wght@300;400;600&display=swap" rel="stylesheet">
<style>
  :root {
    --page: #ffffff;
    --sky-top: #b2e7fb;
    --sky-bottom: #f2fbfe;
    --wave-white: #ffffff;
    --wave-blue: #0869c9;
    --wave-deep: #0557a9;
    --ink: #0a5cb4;
    --mark: #43b9f0;
    --light-text: #ffffff;
  }
  * { margin: 0; padding: 0; box-sizing: border-box; }
  html, body { width: 1200px; height: 1000px; overflow: hidden; background: var(--page); }
  body { position: relative; font-family: "Josefin Sans", sans-serif; color: var(--ink); }

  .card {
    position: absolute;
    left: 286px;
    width: 629px;
    height: 358px;
    overflow: hidden;
    background: linear-gradient(180deg, var(--sky-top) 0%, var(--sky-bottom) 100%);
    box-shadow: 10px 12px 18px rgba(40, 60, 90, 0.28);
  }
  .card--front { top: 121px; }
  .card--back { top: 521px; }

  .card__waves { position: absolute; inset: 0; width: 629px; height: 358px; }
  .wave--white { fill: var(--wave-white); }
  .wave--blue { fill: var(--wave-blue); }
  .wave--deep { fill: var(--wave-deep); }
  .brand-dot { fill: var(--mark); }

  .person { position: absolute; left: 44px; top: 58px; }
  .person__name { font-size: 30px; font-weight: 600; letter-spacing: 0; line-height: 1; }
  .person__credential { font-weight: 300; }
  .person__role { font-size: 22px; font-weight: 400; letter-spacing: 1.5px; margin-top: 8px; line-height: 1; }

  .contact { position: absolute; left: 46px; top: 136px; font-size: 17.5px; letter-spacing: 0.6px; line-height: 26px; }

  .brand { position: absolute; color: var(--light-text); line-height: 1; }
  .brand__name { font-size: 44px; font-weight: 400; letter-spacing: 2px; }
  .brand__tagline { font-size: 18px; font-weight: 600; letter-spacing: 1px; margin-top: 4px; }
  .card--front .brand { right: 48px; top: 258px; text-align: right; }
  .card--back .brand { left: 36px; top: 258px; }

  .services { position: absolute; left: 257px; top: 48px; }
  .services__title { font-size: 30px; font-weight: 400; letter-spacing: 1px; line-height: 1; margin-bottom: 14px; }
  .services__list { list-style: none; font-size: 21px; letter-spacing: 1.5px; line-height: 27px; }
  .services__list li::before { content: "•"; font-size: 16px; margin-right: 9px; vertical-align: 2px; }
</style>
</head>
<body>

  <section class="card card--front" aria-label="Business card front">
    <svg class="card__waves" viewBox="0 0 629 358" aria-hidden="true">
      <path class="wave--white" d="M0,224 C140,285 300,285 629,147 L629,358 L0,358 Z"/>
      <path class="wave--blue" d="M0,230 C140,292 300,290 629,172 L629,358 L0,358 Z"/>
      <path class="wave--deep" d="M0,302 C170,335 380,335 629,185 L629,358 L0,358 Z"/>
      <circle class="brand-dot" cx="153" cy="272" r="48"/>
    </svg>

    <div class="person">
      <h1 class="person__name">MARISA OKAFOR, <span class="person__credential">MPA</span></h1>
      <p class="person__role">CONSULTANT</p>
    </div>

    <div class="contact">
      <p class="contact__phone">(555) 284-7190</p>
      <p class="contact__email">marisa@lumerantadvising.com</p>
    </div>

    <div class="brand">
      <p class="brand__name">LUMERANT</p>
      <p class="brand__tagline">ADVISING AND COACHING LLC</p>
    </div>
  </section>

  <section class="card card--back" aria-label="Business card back">
    <svg class="card__waves" viewBox="0 0 629 358" aria-hidden="true">
      <path class="wave--white" d="M0,147 C250,230 420,290 629,224 L629,358 L0,358 Z"/>
      <path class="wave--blue" d="M0,172 C250,250 420,300 629,232 L629,358 L0,358 Z"/>
      <path class="wave--deep" d="M0,185 C240,300 450,335 629,300 L629,358 L0,358 Z"/>
      <circle class="brand-dot" cx="477" cy="269" r="48"/>
    </svg>

    <div class="services">
      <h2 class="services__title">SERVICES</h2>
      <ul class="services__list">
        <li>CONSULTANTCY</li>
        <li>TRAINING</li>
        <li>DEIJ</li>
        <li>SDOH</li>
      </ul>
    </div>

    <div class="brand">
      <p class="brand__name">LUMERANT</p>
      <p class="brand__tagline">ADVISING AND COACHING LLC</p>
    </div>
  </section>

</body>
</html>
```